Redesign of iOS App Moriva Tutor

Redesign of existing App Moriva Tutor, an app that helps learning Japanese Kanjis, Hiragana, Katakana.

The functionallity should remain the same as today: the app is free, you may download it at the app store. But: I like the design of my other apps better ;)

Target Market(s)

Students learning Japanese

Industry/Entity Type

Teacher

Font styles to use
Sans Serif

Requirements
Must have
• Moriva Tutor has 7 main screens, all screens has to be designed for iPhone and iPad: Main, Settings, Reading Tests, Writing Tests, Game, Paper Mode, Search
Nice to have
• I like the logo as it is today

```html
<!DOCTYPE html>
<html lang="en">
<head>
<meta charset="utf-8">
<title>Moriva Tutor – App Screens</title>
<link href="https://fonts.googleapis.com/css2?family=Roboto:wght@400;500;700&family=Noto+Sans+JP:wght@400;500&display=swap" rel="stylesheet">
<style>
  :root {
    --page: #eef1f4;
    --screen: #ffffff;
    --sky: #4ec6ea;
    --sky-light: #8fdcf3;
    --sky-dark: #2fb0dc;
    --ink: #222222;
    --ink-soft: #777777;
    --chip-dark: #2b2b2b;
    --chip-grey: #9a9a9a;
    --wrong: #f2493a;
    --known: #3a8fe6;
    --right: #1fbfb0;
    --pick-wrong: #ff5a35;
    --pick-right: #27c3c6;
    --tile-bg: #f0f0f0;
    --line: #dddddd;
  }
  * { box-sizing: border-box; margin: 0; padding: 0; }
  html, body { width: 1200px; height: 824px; overflow: hidden; }
  body {
    background: var(--page);
    font-family: "Roboto", "Noto Sans JP", sans-serif;
    color: var(--ink);
    position: relative;
  }
  .screen {
    position: absolute;
    top: 124px;
    width: 280px;
    height: 504px;
    background: var(--screen);
    display: flex;
    flex-direction: column;
    box-shadow: 0 2px 10px rgba(0,0,0,.12);
    overflow: hidden;
  }
  .screen--menu { left: 86px; }
  .screen--quiz { left: 453px; }
  .screen--write { left: 824px; }

  .status-bar {
    height: 20px;
    display: flex;
    align-items: center;
    justify-content: space-between;
    padding: 0 8px;
    font-size: 9px;
    font-weight: 500;
    flex-shrink: 0;
  }
  .status-bar .carrier { display: flex; align-items: center; gap: 3px; width: 60px; }
  .status-bar .battery { width: 60px; display: flex; justify-content: flex-end; }

  /* Level tabs */
  .level-bar {
    height: 48px;
    flex-shrink: 0;
    background: linear-gradient(160deg, var(--sky-light), var(--sky) 55%, var(--sky-dark));
    display: flex;
    align-items: center;
    justify-content: center;
    gap: 4px;
  }
  .level-tab {
    color: #fff;
    font-size: 15px;
    font-weight: 500;
    width: 28px;
    height: 28px;
    display: flex;
    align-items: center;
    justify-content: center;
  }
  .level-tab--active { border: 1px solid rgba(255,255,255,.8); background: rgba(255,255,255,.15); }

  /* Test list */
  .test-list { flex: 1; padding: 6px 10px 0; display: flex; flex-direction: column; }
  .test-row { flex: 1; display: flex; flex-direction: column; justify-content: center; border-bottom: 1px solid #eeeeee; }
  .test-row__head { display: flex; align-items: center; font-size: 9px; font-weight: 700; height: 12px; }
  .test-row__head .name { flex: 1; }
  .test-row__marks { display: grid; grid-template-columns: repeat(4, 36px); gap: 2px; font-size: 9px; text-align: center; }
  .test-row__body { display: flex; align-items: center; margin-top: 2px; }
  .count-chip {
    background: var(--chip-dark);
    color: #fff;
    font-size: 8px;
    width: 32px;
    height: 11px;
    text-align: right;
    padding-right: 3px;
    line-height: 11px;
  }
  .tests-label { font-size: 8px; margin-left: 4px; flex: 1; }
  .score-boxes { display: grid; grid-template-columns: repeat(4, 36px); gap: 2px; }
  .score {
    height: 13px;
    color: #fff;
    font-size: 8px;
    text-align: right;
    padding-right: 3px;
    line-height: 13px;
  }
  .score--total { background: var(--chip-grey); }
  .score--wrong { background: var(--wrong); }
  .score--known { background: var(--known); }
  .score--right { background: var(--right); }
  .mark--play { color: #999; }
  .mark--wrong { color: var(--wrong); }
  .mark--known { color: var(--known); }
  .mark--right { color: var(--right); font-weight: 700; }

  /* Bottom tab bar */
  .tab-bar {
    height: 28px;
    flex-shrink: 0;
    background: linear-gradient(100deg, var(--sky-light), var(--sky) 40%, var(--sky-dark));
    display: flex;
    align-items: center;
    color: #fff;
    font-size: 9px;
    font-weight: 500;
  }
  .tab-bar span { flex: 1; text-align: center; border-right: 1px solid rgba(255,255,255,.35); line-height: 28px; }
  .tab-bar span:last-child { border-right: 0; }
  .tab-bar .tab-home { flex: 1.4; text-align: left; padding-left: 10px; }
  .tab-bar .tab-gap { flex: 1.2; }
  .tab-bar .tab-kanji { font-family: "Noto Sans JP", sans-serif; font-size: 11px; }

  /* Progress panel */
  .progress-band {
    height: 56px;
    flex-shrink: 0;
    background: linear-gradient(160deg, var(--sky-light), var(--sky) 55%, var(--sky-dark));
    display: flex;
    align-items: center;
    justify-content: center;
  }
  .progress-panel {
    width: 240px;
    height: 38px;
    background: #fff;
    display: grid;
    grid-template-columns: repeat(3, 1fr);
    box-shadow: 0 1px 3px rgba(0,0,0,.2);
  }
  .progress-cell { text-align: center; border-right: 1px solid var(--line); padding-top: 4px; background: linear-gradient(#fff, #eeeeee); }
  .progress-cell:last-child { border-right: 0; }
  .progress-cell .label { font-size: 8px; }
  .progress-cell .value { font-size: 16px; line-height: 20px; }
  .progress-cell--remaining { color: #777; }
  .progress-cell--wrong { color: var(--wrong); }
  .progress-cell--correct { color: var(--right); }

  /* Prompt card */
  .prompt-card {
    height: 62px;
    flex-shrink: 0;
    position: relative;
    background: linear-gradient(170deg, #ffffff 40%, #ececec);
    border-bottom: 1px solid var(--line);
    text-align: center;
    padding-top: 8px;
  }
  .prompt-card .prompt { font-size: 22px; line-height: 28px; }
  .prompt-card .prompt--kanji { font-family: "Noto Sans JP", sans-serif; }
  .prompt-card .reading { font-family: "Noto Sans JP", sans-serif; font-size: 8px; color: #999; }
  .prompt-card .star { position: absolute; right: 14px; top: 14px; }

  /* Answer grid */
  .answer-area { flex: 1; background: #f4f4f4; padding: 18px 18px; }
  .answer-grid { display: grid; grid-template-columns: repeat(3, 1fr); grid-template-rows: repeat(3, 75px); gap: 3px; }
  .answer {
    background: #fff;
    font-size: 9px;
    color: #666;
    display: flex;
    align-items: center;
    justify-content: center;
  }
  .answer--wrong { background: var(--pick-wrong); color: #fff; }
  .answer--right { background: var(--pick-right); color: #fff; }

  /* Writing pad */
  .writing-area { flex: 1; padding: 14px 14px; }
  .writing-pad { width: 252px; height: 288px; border: 1px solid #999; position: relative; }
  .writing-pad svg { position: absolute; inset: 0; }
  .stroke-area {
    position: absolute;
    left: 42px; top: 30px; width: 168px; height: 228px;
    background: radial-gradient(ellipse at center, rgba(30,30,30,.25), rgba(200,200,200,.15) 65%, transparent 75%);
  }
</style>
</head>
<body>

  <!-- Main menu -->
  <section class="screen screen--menu">
    <div class="status-bar">
      <span class="carrier">Carrier
        <svg width="9" height="7" viewBox="0 0 9 7"><path d="M4.5 7 L0.5 2.5 A6 6 0 0 1 8.5 2.5 Z" fill="#222"/></svg>
      </span>
      <span>1:21 PM</span>
      <span class="battery"><svg width="18" height="8" viewBox="0 0 18 8"><rect x="0.5" y="0.5" width="15" height="7" fill="none" stroke="#222"/><rect x="2" y="2" width="12" height="4" fill="#222"/><rect x="16" y="2.5" width="1.5" height="3" fill="#222"/></svg></span>
    </div>
    <nav class="level-bar">
      <span class="level-tab">K</span>
      <span class="level-tab level-tab--active">N5</span>
      <span class="level-tab">N4</span>
      <span class="level-tab">N3</span>
      <span class="level-tab">N2</span>
      <span class="level-tab">N1</span>
      <span class="level-tab">★</span>
    </nav>
    <div class="test-list">
      <div class="test-row">
        <div class="test-row__head"><span class="name">Kanji → Meaning</span>
          <span class="test-row__marks"><span class="mark--play">▸</span><span class="mark--wrong">✕</span><span class="mark--known">○</span><span class="mark--right">✓</span></span></div>
        <div class="test-row__body"><span class="count-chip">103</span><span class="tests-label">Tests</span>
          <span class="score-boxes"><span class="score score--total">103</span><span class="score score--wrong">0</span><span class="score score--known">0</span><span class="score score--right">0</span></span></div>
      </div>
      <div class="test-row">
        <div class="test-row__head"><span class="name">Meaning → Kanji</span></div>
        <div class="test-row__body"><span class="count-chip">103</span><span class="tests-label">Tests</span>
          <span class="score-boxes"><span class="score score--total">103</span><span class="score score--wrong">0</span><span class="score score--known">0</span><span class="score score--right">0</span></span></div>
      </div>
      <div class="test-row">
        <div class="test-row__head"><span class="name">Kanji → On</span></div>
        <div class="test-row__body"><span class="count-chip">103</span><span class="tests-label">Tests</span>
          <span class="score-boxes"><span class="score score--total">103</span><span class="score score--wrong">0</span><span class="score score--known">0</span><span class="score score--right">0</span></span></div>
      </div>
      <div class="test-row">
        <div class="test-row__head"><span class="name">On → Kanji</span></div>
        <div class="test-row__body"><span class="count-chip">103</span><span class="tests-label">Tests</span>
          <span class="score-boxes"><span class="score score--total">103</span><span class="score score--wrong">0</span><span class="score score--known">0</span><span class="score score--right">0</span></span></div>
      </div>
      <div class="test-row">
        <div class="test-row__head"><span class="name">Kanji → Kun</span></div>
        <div class="test-row__body"><span class="count-chip">94</span><span class="tests-label">Tests</span>
          <span class="score-boxes"><span class="score score--total">94</span><span class="score score--wrong">0</span><span class="score score--known">0</span><span class="score score--right">0</span></span></div>
      </div>
      <div class="test-row">
        <div class="test-row__head"><span class="name">Kun → Kanji</span></div>
        <div class="test-row__body"><span class="count-chip">94</span><span class="tests-label">Tests</span>
          <span class="score-boxes"><span class="score score--total">94</span><span class="score score--wrong">0</span><span class="score score--known">0</span><span class="score score--right">0</span></span></div>
      </div>
      <div class="test-row">
        <div class="test-row__head"><span class="name">Word → Reading</span></div>
        <div class="test-row__body"><span class="count-chip">582</span><span class="tests-label">Tests</span>
          <span class="score-boxes"><span class="score score--total">582</span><span class="score score--wrong">0</span><span class="score score--known">0</span><span class="score score--right">0</span></span></div>
      </div>
      <div class="test-row">
        <div class="test-row__head"><span class="name">Reading → Word</span></div>
        <div class="test-row__body"><span class="count-chip">582</span><span class="tests-label">Tests</span>
          <span class="score-boxes"><span class="score score--total">582</span><span class="score score--wrong">0</span><span class="score score--known">0</span><span class="score score--right">0</span></span></div>
      </div>
      <div class="test-row">
        <div class="test-row__head"><span class="name">Writing</span></div>
        <div class="test-row__body"><span class="count-chip">103</span><span class="tests-label">Tests</span>
          <span class="score-boxes"><span class="score score--total">103</span><span class="score score--wrong">0</span><span class="score score--known">0</span><span class="score score--right">0</span></span></div>
      </div>
      <div class="test-row">
        <div class="test-row__head"><span class="name">All Tests</span></div>
        <div class="test-row__body"><span class="count-chip">1867</span><span class="tests-label">Tests</span>
          <span class="score-boxes"><span class="score score--total">1867</span><span class="score score--wrong">0</span><span class="score score--known">0</span><span class="score score--right">0</span></span></div>
      </div>
    </div>
    <nav class="tab-bar">
      <span>SETTINGS</span><span>SEARCH</span><span>GAME</span><span>PAPER</span>
    </nav>
  </section>

  <!-- Reading test -->
  <section class="screen screen--quiz">
    <div class="status-bar">
      <span class="carrier">Carrier
        <svg width="9" height="7" viewBox="0 0 9 7"><path d="M4.5 7 L0.5 2.5 A6 6 0 0 1 8.5 2.5 Z" fill="#222"/></svg>
      </span>
      <span>1:21 PM</span>
      <span class="battery"><svg width="18" height="8" viewBox="0 0 18 8"><rect x="0.5" y="0.5" width="15" height="7" fill="none" stroke="#222"/><rect x="2" y="2" width="12" height="4" fill="#222"/><rect x="16" y="2.5" width="1.5" height="3" fill="#222"/></svg></span>
    </div>
    <div class="progress-band">
      <div class="progress-panel">
        <div class="progress-cell progress-cell--remaining"><div class="label">Remaining</div><div class="value">102</div></div>
        <div class="progress-cell progress-cell--wrong"><div class="label">Wrong</div><div class="value">1</div></div>
        <div class="progress-cell progress-cell--correct"><div class="label">Correct</div><div class="value">0</div></div>
      </div>
    </div>
    <div class="prompt-card">
      <div class="prompt prompt--kanji">名</div>
      <div class="reading">メイ, ミョウ, な</div>
      <svg class="star" width="16" height="16" viewBox="0 0 24 24"><path d="M12 2.5 L14.8 9 L21.8 9.5 L16.4 14 L18.1 21 L12 17.2 L5.9 21 L7.6 14 L2.2 9.5 L9.2 9 Z" fill="none" stroke="#222" stroke-width="1.6" stroke-linejoin="round"/></svg>
    </div>
    <div class="answer-area">
      <div class="answer-grid">
        <div class="answer">Seven</div>
        <div class="answer answer--wrong">person</div>
        <div class="answer">long</div>
        <div class="answer answer--right">name</div>
        <div class="answer">come</div>
        <div class="answer">many</div>
        <div class="answer">white</div>
        <div class="answer">in</div>
        <div class="answer">Station</div>
      </div>
    </div>
    <nav class="tab-bar">
      <span class="tab-home">HOME</span><span class="tab-gap"></span><span class="tab-kanji">名</span><span>SKIP</span>
    </nav>
  </section>

  <!-- Writing test -->
  <section class="screen screen--write">
    <div class="status-bar">
      <span class="carrier">Carrier
        <svg width="9" height="7" viewBox="0 0 9 7"><path d="M4.5 7 L0.5 2.5 A6 6 0 0 1 8.5 2.5 Z" fill="#222"/></svg>
      </span>
      <span>1:21 PM</span>
      <span class="battery"><svg width="18" height="8" viewBox="0 0 18 8"><rect x="0.5" y="0.5" width="15" height="7" fill="none" stroke="#222"/><rect x="2" y="2" width="12" height="4" fill="#222"/><rect x="16" y="2.5" width="1.5" height="3" fill="#222"/></svg></span>
    </div>
    <div class="progress-band">
      <div class="progress-panel">
        <div class="progress-cell progress-cell--remaining"><div class="label">Remaining</div><div class="value">102</div></div>
        <div class="progress-cell progress-cell--wrong"><div class="label">Wrong</div><div class="value">1</div></div>
        <div class="progress-cell progress-cell--correct"><div class="label">Correct</div><div class="value">0</div></div>
      </div>
    </div>
    <div class="prompt-card">
      <div class="prompt">fire</div>
      <div class="reading">カ, ひ</div>
      <svg class="star" width="16" height="16" viewBox="0 0 24 24"><path d="M12 2.5 L14.8 9 L21.8 9.5 L16.4 14 L18.1 21 L12 17.2 L5.9 21 L7.6 14 L2.2 9.5 L9.2 9 Z" fill="none" stroke="#222" stroke-width="1.6" stroke-linejoin="round"/></svg>
    </div>
    <div class="writing-area">
      <div class="writing-pad">
        <svg width="250" height="286" viewBox="0 0 250 286">
          <line x1="125" y1="0" x2="125" y2="286" stroke="#999" stroke-width="1"/>
          <line x1="0" y1="143" x2="250" y2="143" stroke="#999" stroke-width="1"/>
        </svg>
        <div class="stroke-area" role="img" aria-label="Handwritten strokes of the kanji for fire, with a faint guide stroke"></div>
      </div>
    </div>
    <nav class="tab-bar">
      <span class="tab-home">HOME</span><span class="tab-gap"></span><span class="tab-kanji">火</span><span>NEXT</span>
    </nav>
  </section>

</body>
</html>
```